Tarvel Key Works

The wrap i would like to have designed is for a 2022 Kelvor Drayline 2600. Half to 3/4 of the van wrapped, my logo & Phone number on the attachment along with the other logos on attachment i would like included in your design unless its to busy. As far as colors ill leave up to you the designer. Realistic images of vehicle keys & Fobs as well. thank you.

```html
<!DOCTYPE html>
<html lang="en">
<head>
<meta charset="utf-8">
<title>Tarvel Key Works – Van Wrap</title>
<link href="https://fonts.googleapis.com/css2?family=Audiowide&family=Oswald:wght@300;700&display=swap" rel="stylesheet">
<style>
  :root{
    --bg:#0c3537;
    --van:#ffffff;
    --line:#c9c9c9;
    --ink:#0a0a0a;
    --cyan:#3ee4ee;
    --glass:#dcdcdc;
    --lamp:#eef07a;
    --wrap-dark:#8c8c8c;
    --hub:#b9b9b9;
  }
  html,body{margin:0;padding:0;overflow:hidden;background:var(--bg);}
  .canvas{width:1200px;height:1171px;position:relative;background:var(--bg);}
  .canvas svg{display:block;}
  .brand-name{font-family:"Audiowide",sans-serif;fill:var(--ink);}
  .tagline{font-family:"Audiowide",sans-serif;font-size:15px;fill:var(--ink);letter-spacing:.5px;}
  .tagline-accent{font-family:"Audiowide",sans-serif;font-size:25px;fill:var(--cyan);stroke:var(--ink);stroke-width:.8px;paint-order:stroke;letter-spacing:1px;}
  .phone-number{font-family:"Oswald",sans-serif;font-weight:700;font-size:60px;fill:var(--cyan);stroke:var(--ink);stroke-width:3px;paint-order:stroke;}
  .web{font-family:"Oswald",sans-serif;font-weight:300;font-size:25px;fill:var(--ink);}
  .web .accent{fill:var(--cyan);}
  .model-badge{font-family:"Audiowide",sans-serif;fill:var(--ink);}
</style>
</head>
<body>
<div class="canvas">
<svg width="1200" height="1171" viewBox="0 0 1200 1171" xmlns="http://www.w3.org/2000/svg">
  <defs>
    <clipPath id="van-body">
      <path d="M92 398 L660 393 L810 410 L985 547 L1088 643 L1125 700 L1133 785 L1130 797 L95 797 L92 700 Z"/>
    </clipPath>
    <linearGradient id="wrap-fade" x1="0" x2="1" y1="0" y2="0">
      <stop offset="0" stop-color="var(--wrap-dark)"/>
      <stop offset="0.55" stop-color="#c8c8c8"/>
      <stop offset="1" stop-color="#ffffff"/>
    </linearGradient>
    <linearGradient id="fob-tone" x1="0" x2="1" y1="0" y2="1">
      <stop offset="0" stop-color="#3a3a3a"/>
      <stop offset="0.5" stop-color="#8a8a8a"/>
      <stop offset="1" stop-color="#2a2a2a"/>
    </linearGradient>
  </defs>

  <!-- van body -->
  <g class="van">
    <path d="M92 398 L660 393 L810 410 L985 547 L1088 643 L1125 700 L1133 785 L1130 797 L95 797 L92 700 Z" fill="var(--van)" stroke="var(--line)"/>
    <g clip-path="url(#van-body)">
      <rect class="wrap-panel" x="80" y="380" width="585" height="430" fill="url(#wrap-fade)"
            role="img" aria-label="Faint repeating pattern of key fob outlines across the wrap"/>
    </g>
    <path class="side-window" d="M694 440 L790 436 L944 560 L940 602 L700 592 Z" fill="var(--glass)" stroke="var(--line)"/>
    <path class="mirror" d="M858 520 L880 518 L890 592 L862 595 Z" fill="#3a3a3a"/>
    <path class="headlight" d="M978 575 L1040 598 L1074 636 L1030 638 L982 600 Z" fill="var(--lamp)"/>
    <rect class="door-handle" x="697" y="590" width="22" height="38" rx="6" fill="none" stroke="var(--line)"/>
    <path class="side-stripe" d="M385 728 L793 728 L785 766 L395 766 Z" fill="var(--ink)"/>
    <rect x="1098" y="708" width="30" height="22" rx="3" fill="#222"/>
    <rect x="1076" y="757" width="54" height="24" rx="6" fill="#222"/>
  </g>

  <!-- wheels -->
  <g class="wheels">
    <circle cx="291" cy="780" r="88" fill="var(--bg)"/>
    <circle cx="930" cy="780" r="88" fill="var(--bg)"/>
    <rect x="190" y="797" width="200" height="20" fill="var(--bg)"/>
    <rect x="830" y="797" width="200" height="20" fill="var(--bg)"/>
    <circle cx="291" cy="780" r="75" fill="var(--ink)"/>
    <circle cx="291" cy="780" r="46" fill="var(--hub)"/>
    <circle cx="291" cy="780" r="8" fill="#555"/>
    <circle cx="930" cy="780" r="75" fill="var(--ink)"/>
    <circle cx="930" cy="780" r="46" fill="var(--hub)"/>
    <circle cx="930" cy="780" r="8" fill="#555"/>
  </g>

  <!-- brand -->
  <g class="brand">
    <text class="brand-name" x="148" y="545" font-size="48">TARVEL</text>
    <text class="brand-name" x="148" y="585" font-size="32">KEY WORKS</text>
  </g>

  <!-- tagline -->
  <text class="tagline" x="314" y="452">YOUR TRUSTWORTH CHOICE FOR YOUR</text>
  <text class="tagline-accent" x="340" y="479">LOCK &amp; KEY NEEDS</text>

  <!-- key fobs -->
  <rect class="key-photo" x="448" y="489" width="148" height="100" rx="18" fill="url(#fob-tone)"
        role="img" aria-label="Photo of two vehicle smart key fobs"/>

  <!-- contact -->
  <g class="phone-icon">
    <circle cx="328" cy="628" r="14" fill="var(--ink)"/>
    <path d="M322 620 q-3 4 1 10 q5 7 10 6 l2 -4 l-4 -3 l-2 2 q-4 -2 -6 -6 l2 -2 l-2 -4 z" fill="#fff"/>
  </g>
  <text class="phone-number" x="356" y="650">505.555.0148</text>
  <text class="web" x="313" y="684">tarvel<tspan class="accent">keyworks</tspan>.org</text>

  <!-- partner badges -->
  <rect class="badge" x="530" y="660" width="65" height="60" rx="4" fill="#d9d9d9"
        role="img" aria-label="Vehicle security professional badge"/>
  <circle class="badge" cx="627" cy="690" r="30" fill="#d63a3a"
          role="img" aria-label="Trusted locksmiths association badge"/>

  <!-- model badge -->
  <g class="model-badge">
    <text x="912" y="616" font-size="8">KELVOR</text>
    <text x="912" y="627" font-size="10">2600</text>
    <text x="912" y="634" font-size="5">DRAYLINE</text>
  </g>
</svg>
</div>
</body>
</html>
```